依頼詳細
【背景】
弊社は平成17年の創業以来、パチンコ店の広告物を主に企画提案〜制作、折込などの代理店業を行ってきました。
しかし、パチンコ業界の規制強化などの理由から、パチンコ業界以外の業種の広告物やBtoBの販促企画•制作、また最近では農家のブランディングなどの仕事にシフトしてきています。
そのような状況の中、弊社の代表自らもMBAのビジネススクールに通いマーケティング等を学び直しており、今後は現状の制作メインの仕事だけではなく、さらに川上のマーケティングや広告戦略といった、もっとクライアントに入り込んだお手伝いが出来る力をつけていきたいと考えています。
その為には再度、組織の再構築、強みを活かせる組織づくりを行っていく必要があり、設立10年を前に第二創業といった心づもりで企業理念を変更しようと考えています。
また、企業理念はこの会社は何の為に存在しているのかを言語化したものであり、在職中のスタッフだけではなく、今後採用予定の方にも共感した上で働いていただきたいと考えています。

【仕様】
・A3縦で制作してください
・納品はイラレデータでお願いします
・イメージは実際の経営理念から想像してください
記載項目
企業理念

Creative Happy!
-社会のHappy!
-顧客のHappy!
-仲間のHappy!
-家族のHappy!
-自分のHappy!

会社ロゴ

【解説(ココは記載不要です)】
Creative Happy! … 広告物を作るのではなく、その先にあるHappyを作っているという意識。
例えば、ケーキ屋さんのDMを作る際、「ケーキ屋さんのDMをつくっている」という意識ではなく「家族で美味しそうにこのケーキを食べている姿」つまり「その先のHappy!」を意識・想像して作ることが出来れば、仕事の質に大きな差が生じると考えています。

-社会のHappy!
-顧客のHappy!
-仲間のHappy!
-家族のHappy!
-自分のHappy!
仕事をする上で「Happy!を考える順番」を意味しています。
希望イメージ
シンプル 複雑
単色 カラフル
暗い 明るい
日常 高級
遊び心 厳粛
未来的 伝統的
女性的 男性的
希望する色
納品ファイル
• イラストレーター形式 (.ai)
補足説明
■ 選んだ理由

まずイメージが明るくHAPPYな感じがしたこと
次に非常にわかりやすいビジュアルでストーリーを作ってくださったことが
kitazono-teさんのデザインを選んだ理由です。

■ 提案者全員のお礼・コメント

皆様にはご提案をいただき感謝いたします。
今回、大変多くの方からご提案をいただき、素敵なデザインが他にもあり社内でも選考するのに随分意見が出ました。

今回は弊社の社内的なポスターでしたが、弊社は広告代理業を行っているためチラシやDMなど他のグラフィックデザインも仕事として発生しています。(携帯電話のチラシなど)
またお願いすることもあるかと思いますので、どうぞよろしくお願いします。

```html
<!DOCTYPE html>
<html lang="ja">
<head>
<meta charset="utf-8">
<title>Creative Happy! 企業理念ポスター</title>
<link rel="stylesheet" href="https://fonts.googleapis.com/css2?family=Francois+One&family=Noto+Sans+JP:wght@900&display=swap">
<style>
  :root {
    --bg-grey: #a59e97;
    --lime: #c3d21f;
    --white: #ffffff;
    --ink: #1a1a1a;
    --title-red: #e60f1e;
    --panel-red: #e2141e;
    --panel-navy: #1d3a5c;
    --panel-yellow: #f6c200;
    --panel-magenta: #b8167c;
    --panel-green: #79b83a;
    --smile-yellow: #f7cf16;
  }
  html, body {
    margin: 0;
    padding: 0;
    width: 849px;
    height: 1200px;
    overflow: hidden;
    background: var(--bg-grey);
  }
  .poster {
    display: block;
    width: 849px;
    height: 1200px;
  }
  .backdrop { fill: var(--bg-grey); }
  .title-band { fill: var(--lime); }
  .title-box { fill: var(--white); }
  .title-text {
    font-family: "Francois One", sans-serif;
    font-size: 112px;
    fill: var(--title-red);
    stroke: var(--ink);
    stroke-width: 3px;
    paint-order: stroke fill;
    text-anchor: middle;
  }
  .panel-red { fill: var(--panel-red); }
  .panel-navy { fill: var(--panel-navy); }
  .panel-yellow { fill: var(--panel-yellow); }
  .panel-magenta { fill: var(--panel-magenta); }
  .panel-green { fill: var(--panel-green); }
  .smile {
    fill: var(--smile-yellow);
    stroke: var(--ink);
    stroke-width: 4px;
  }
  .bubble {
    fill: var(--white);
    stroke: var(--ink);
    stroke-width: 4px;
    stroke-linejoin: round;
  }
  .happy {
    font-family: "Francois One", sans-serif;
    fill: var(--ink);
    text-anchor: middle;
  }
  .word, .particle {
    font-family: "Noto Sans JP", sans-serif;
    font-weight: 900;
    fill: var(--ink);
    text-anchor: middle;
  }
  .brand-name {
    font-family: "Francois One", sans-serif;
    font-size: 62px;
    fill: var(--ink);
    text-anchor: middle;
  }
</style>
</head>
<body>
<svg class="poster" viewBox="0 0 849 1200" xmlns="http://www.w3.org/2000/svg">
  <rect class="backdrop" width="849" height="1200"/>

  <g class="title">
    <rect class="title-band" x="28" y="22" width="793" height="150"/>
    <rect class="title-box" x="48" y="40" width="753" height="114"/>
    <text class="title-text" x="424.5" y="136" textLength="720" lengthAdjust="spacingAndGlyphs">Creative Happy!</text>
  </g>

  <g class="scene scene-society">
    <polygon class="panel-red" points="34,226 428,226 428,572 34,592"/>
    <circle class="smile" cx="232" cy="336" r="100" role="img" aria-label="黄色い丸いキャラクター"/>
    <text class="happy" x="232" y="372" font-size="50">Happy!</text>
    <path class="bubble" d="M60,520 C40,460 100,430 150,440 C175,420 210,425 205,445 C230,470 220,545 160,565 C110,585 70,560 60,520 Z"/>
    <text class="word" x="135" y="525" font-size="62">社会</text>
    <text class="particle" x="135" y="560" font-size="24">の</text>
  </g>

  <g class="scene scene-client">
    <polygon class="panel-navy" points="440,226 815,226 815,520 440,545"/>
    <circle class="smile" cx="584" cy="366" r="92" role="img" aria-label="黄色い丸いキャラクター"/>
    <text class="happy" x="584" y="400" font-size="46">Happy!</text>
    <path class="bubble" d="M722,232 C780,232 790,300 785,350 C782,420 760,460 722,462 C700,470 680,480 664,486 C676,468 680,455 678,440 C660,400 660,300 672,270 C680,245 700,232 722,232 Z"/>
    <text class="word" x="726" y="310" font-size="62">顧</text>
    <text class="word" x="726" y="378" font-size="62">客</text>
    <text class="particle" x="726" y="428" font-size="28">の</text>
  </g>

  <g class="brand">
    <text class="brand-name" x="647" y="624" textLength="316" lengthAdjust="spacingAndGlyphs">LUMEN WORKS</text>
  </g>

  <g class="scene scene-team">
    <polygon class="panel-yellow" points="34,668 815,642 815,815 34,832"/>
    <path class="bubble" d="M350,750 C350,705 410,690 460,692 C520,694 565,712 568,742 C600,752 618,760 630,765 C610,768 590,772 566,772 C550,800 500,812 455,810 C395,808 350,790 350,750 Z"/>
    <text class="word" x="440" y="775" font-size="60">仲間</text>
    <text class="particle" x="534" y="772" font-size="26">の</text>
    <circle class="smile" cx="710" cy="760" r="84" role="img" aria-label="黄色い丸いキャラクター"/>
    <text class="happy" x="710" y="792" font-size="42">Happy!</text>
  </g>

  <g class="scene scene-family">
    <polygon class="panel-magenta" points="34,858 505,858 505,1167 34,1167"/>
    <path class="bubble" d="M128,878 C188,878 198,950 196,1000 C194,1060 180,1110 140,1118 C150,1135 160,1145 175,1152 C145,1148 125,1138 112,1120 C70,1108 58,1050 60,990 C62,930 75,878 128,878 Z"/>
    <text class="word" x="128" y="958" font-size="62">家</text>
    <text class="word" x="128" y="1028" font-size="62">族</text>
    <text class="particle" x="128" y="1080" font-size="28">の</text>
    <circle class="smile" cx="345" cy="1060" r="102" role="img" aria-label="黄色い丸いキャラクター"/>
    <text class="happy" x="345" y="1098" font-size="52">Happy!</text>
  </g>

  <g class="scene scene-self">
    <polygon class="panel-green" points="540,884 815,872 815,1167 540,1167"/>
    <circle class="smile" cx="630" cy="968" r="80" role="img" aria-label="黄色い丸いキャラクター"/>
    <text class="happy" x="630" y="998" font-size="40">Happy!</text>
    <path class="bubble" d="M680,1080 C680,1040 715,1025 748,1028 C790,1030 810,1055 808,1088 C806,1120 780,1140 748,1140 C740,1152 730,1160 715,1166 C722,1155 724,1145 722,1138 C696,1128 680,1108 680,1080 Z"/>
    <text class="word" x="745" y="1098" font-size="48">自分</text>
    <text class="particle" x="745" y="1128" font-size="22">の</text>
  </g>
</svg>
</body>
</html>
```